Arvo 7 Detection Wheel

We need a professional **framework wheel diagram** designed for our detection dog training manual.

Our business is **Arvo 7 Dog Training**, and this graphic represents our **Detection Training Model**.

Please use the **attached reference images** as a guide for the structure and layout of the wheel.

### What we need

1. **Full wheel graphic**

* Clean circular framework wheel
* Similar structure to the attached example
* Clear sections and text
* Professional training manual style
* Transparent background

2. **Individual segment pieces**

We also need the **inner sections broken into separate pieces** (like the second reference image).

This will allow us to place each section on different pages of the manual when explaining the concepts.

Each piece should look like a **slice of the wheel**.

### Style

The design should look:

• Professional
• Clean and modern
• Structured and easy to read
• Suitable for a training manual

Avoid cartoon styles or clipart.

### Colours

Please use our brand colour palette (see attached image):

* Dark navy blue
* Steel blue
* Light blue
* White
* Light grey
* Dark grey

### Files required

Final files must include:

* Vector files (AI or EPS)
* Transparent PNG
* High-resolution PDF

Please also provide **each segment exported individually**

```html
<!DOCTYPE html>
<html lang="en">
<head>
<meta charset="utf-8">
<title>Arvo 7 Detection Wheel</title>
<link rel="stylesheet" href="https://fonts.googleapis.com/css2?family=Barlow+Condensed:wght@600&family=Fira+Sans:wght@600&display=swap">
<style>
  :root {
    --steel: #5d9bb6;
    --sky: #78bee0;
    --navy-text: #2f5d78;
    --label-blue: #4f8fae;
    --band: #edf4f8;
    --ink-grey: #555a5e;
    --soft-grey: #d9dcde;
    --white: #ffffff;
  }
  html, body {
    margin: 0;
    padding: 0;
    width: 1200px;
    height: 1200px;
    overflow: hidden;
    background: var(--white);
  }
  .detection-wheel { display: block; width: 1200px; height: 1200px; }
  .seg-steel { fill: var(--steel); }
  .seg-sky { fill: var(--sky); }
  .band { fill: var(--band); }
  .divider { stroke: var(--white); stroke-width: 8; stroke-linecap: round; }
  .ring-label {
    font-family: "Fira Sans", sans-serif;
    font-weight: 600;
    font-size: 22px;
    letter-spacing: 3.5px;
  }
  .ring-label.on-steel { fill: var(--white); }
  .ring-label.on-sky { fill: var(--navy-text); }
  .zone-label {
    font-family: "Fira Sans", sans-serif;
    font-weight: 600;
    font-size: 24px;
    letter-spacing: 5px;
    fill: var(--label-blue);
  }
  .area-label {
    font-family: "Fira Sans", sans-serif;
    font-weight: 600;
    font-size: 26px;
    letter-spacing: 5px;
    fill: var(--label-blue);
  }
  .slice-label {
    font-family: "Barlow Condensed", sans-serif;
    font-weight: 600;
    text-anchor: middle;
    dominant-baseline: central;
  }
  .slice-label.dog { fill: var(--white); font-size: 20px; }
  .slice-label.handler { fill: var(--navy-text); font-size: 24px; }
  .slice-label.handler.large { font-size: 28px; }
  .cycle-arc { fill: none; stroke: var(--ink-grey); stroke-width: 2.5; }
  .cycle-head { fill: none; stroke: var(--ink-grey); stroke-width: 2.5; stroke-linecap: round; stroke-linejoin: round; }
  .cycle-dot { fill: var(--ink-grey); }
  .inner-arc { fill: none; stroke: var(--ink-grey); stroke-width: 2.5; }
  .hub { fill: var(--white); stroke: var(--soft-grey); stroke-width: 2; }
  .hub-name {
    font-family: "Barlow Condensed", sans-serif;
    font-weight: 600;
    font-size: 32px;
    letter-spacing: 2px;
    fill: var(--label-blue);
    text-anchor: middle;
    dominant-baseline: central;
  }
  .backdrop { opacity: 0.12; }
</style>
</head>
<body>
<svg class="detection-wheel" viewBox="0 0 1200 1200" xmlns="http://www.w3.org/2000/svg" role="img" aria-label="Arvo 7 detection training model wheel">
  <defs>
    <!-- text paths: outer ring -->
    <path id="tp-integrity" d="M275 600 A325 325 0 0 1 370.2 370.2"/>
    <path id="tp-development" d="M370.2 370.2 A325 325 0 0 1 600 275"/>
    <path id="tp-distractions" d="M600 275 A325 325 0 0 1 829.8 370.2"/>
    <path id="tp-behaviour" d="M829.8 370.2 A325 325 0 0 1 925 600"/>
    <path id="tp-deployment" d="M257 600 A343 343 0 0 0 357.5 842.5"/>
    <path id="tp-reinforcement" d="M357.5 842.5 A343 343 0 0 0 600 943"/>
    <path id="tp-search-method" d="M600 943 A343 343 0 0 0 842.5 842.5"/>
    <path id="tp-target-odour" d="M842.5 842.5 A343 343 0 0 0 943 600"/>
    <!-- text paths: zones and areas -->
    <path id="tp-dog-foundations" d="M384.8 521.7 A229 229 0 0 1 815.2 521.7"/>
    <path id="tp-handler-foundations" d="M360.4 687.2 A255 255 0 0 0 839.6 687.2"/>
    <path id="tp-area-top" d="M230.7 465.6 A393 393 0 0 1 969.3 465.6"/>
    <path id="tp-area-bottom" d="M210 741.9 A415 415 0 0 0 990 741.9"/>

    <g id="wheel-core">
      <circle class="band" cx="600" cy="600" r="282"/>

      <!-- outer ring: operational capability areas -->
      <g class="outer-ring">
        <path class="seg-steel" d="M212 600 A388 388 0 0 1 325.6 325.6 L402 402 A280 280 0 0 0 320 600 Z"/>
        <path class="seg-steel" d="M325.6 325.6 A388 388 0 0 1 600 212 L600 320 A280 280 0 0 0 402 402 Z"/>
        <path class="seg-sky" d="M600 212 A388 388 0 0 1 874.4 325.6 L798 402 A280 280 0 0 0 600 320 Z"/>
        <path class="seg-sky" d="M874.4 325.6 A388 388 0 0 1 988 600 L880 600 A280 280 0 0 0 798 402 Z"/>
        <path class="seg-steel" d="M988 600 A388 388 0 0 1 874.4 874.4 L798 798 A280 280 0 0 0 880 600 Z"/>
        <path class="seg-steel" d="M874.4 874.4 A388 388 0 0 1 600 988 L600 880 A280 280 0 0 0 798 798 Z"/>
        <path class="seg-sky" d="M600 988 A388 388 0 0 1 325.6 874.4 L402 798 A280 280 0 0 0 600 880 Z"/>
        <path class="seg-sky" d="M325.6 874.4 A388 388 0 0 1 212 600 L320 600 A280 280 0 0 0 402 798 Z"/>
        <g class="outer-dividers">
          <line class="divider" x1="795.2" y1="795.2" x2="877.2" y2="877.2"/>
          <line class="divider" x1="404.8" y1="795.2" x2="322.8" y2="877.2"/>
          <line class="divider" x1="404.8" y1="404.8" x2="322.8" y2="322.8"/>
          <line class="divider" x1="795.2" y1="404.8" x2="877.2" y2="322.8"/>
          <line class="divider" x1="876" y1="600" x2="992" y2="600"/>
          <line class="divider" x1="208" y1="600" x2="324" y2="600"/>
          <line class="divider" x1="600" y1="876" x2="600" y2="992"/>
          <line class="divider" x1="600" y1="208" x2="600" y2="324"/>
        </g>
        <text class="ring-label on-steel"><textPath href="#tp-integrity" startOffset="50%" text-anchor="middle">INTEGRITY</textPath></text>
        <text class="ring-label on-steel"><textPath href="#tp-development" startOffset="50%" text-anchor="middle">DEVELOPMENT</textPath></text>
        <text class="ring-label on-sky"><textPath href="#tp-distractions" startOffset="50%" text-anchor="middle">DISTRACTIONS</textPath></text>
        <text class="ring-label on-sky"><textPath href="#tp-behaviour" startOffset="50%" text-anchor="middle">BEHAVIOUR</textPath></text>
        <text class="ring-label on-sky"><textPath href="#tp-deployment" startOffset="50%" text-anchor="middle">DEPLOYMENT</textPath></text>
        <text class="ring-label on-sky"><textPath href="#tp-reinforcement" startOffset="50%" text-anchor="middle">REINFORCEMENT</textPath></text>
        <text class="ring-label on-steel"><textPath href="#tp-search-method" startOffset="50%" text-anchor="middle">SEARCH METHOD</textPath></text>
        <text class="ring-label on-steel"><textPath href="#tp-target-odour" startOffset="50%" text-anchor="middle">TARGET ODOUR</textPath></text>
      </g>

      <!-- inner slices: dog and handler foundations -->
      <g class="inner-slices">
        <path class="seg-steel" d="M600 600 L383 600 A217 217 0 0 1 424.4 472.4 Z"/>
        <path class="seg-steel" d="M600 600 L424.4 472.4 A217 217 0 0 1 532.9 393.6 Z"/>
        <path class="seg-steel" d="M600 600 L532.9 393.6 A217 217 0 0 1 667.1 393.6 Z"/>
        <path class="seg-steel" d="M600 600 L667.1 393.6 A217 217 0 0 1 775.6 472.4 Z"/>
        <path class="seg-steel" d="M600 600 L775.6 472.4 A217 217 0 0 1 817 600 Z"/>
        <path class="seg-sky" d="M600 600 L817 600 A217 217 0 0 1 753.4 753.4 Z"/>
        <path class="seg-sky" d="M600 600 L753.4 753.4 A217 217 0 0 1 600 817 Z"/>
        <path class="seg-sky" d="M600 600 L600 817 A217 217 0 0 1 446.6 753.4 Z"/>
        <path class="seg-sky" d="M600 600 L446.6 753.4 A217 217 0 0 1 383 600 Z"/>
        <g class="inner-dividers">
          <line class="divider" x1="375" y1="600" x2="825" y2="600"/>
          <line class="divider" x1="600" y1="600" x2="418" y2="467.7"/>
          <line class="divider" x1="600" y1="600" x2="530.5" y2="386"/>
          <line class="divider" x1="600" y1="600" x2="669.5" y2="386"/>
          <line class="divider" x1="600" y1="600" x2="782" y2="467.7"/>
          <line class="divider" x1="600" y1="600" x2="759.1" y2="759.1"/>
          <line class="divider" x1="600" y1="600" x2="600" y2="825"/>
          <line class="divider" x1="600" y1="600" x2="440.9" y2="759.1"/>
        </g>

        <text class="slice-label dog"><tspan x="447" y="547">GENETIC</tspan><tspan x="447" y="569">SUITABILITY</tspan></text>
        <text class="slice-label dog"><tspan x="503" y="447">HEALTH &amp;</tspan><tspan x="503" y="469">PHYSICAL</tspan><tspan x="503" y="491">WELLBEING</tspan></text>
        <text class="slice-label dog"><tspan x="600" y="413">ENGAGEMENT</tspan><tspan x="600" y="435">RELATIONSHIP</tspan></text>
        <text class="slice-label dog"><tspan x="696" y="469">REWARD</tspan><tspan x="696" y="491">VALUE</tspan></text>
        <text class="slice-label dog"><tspan x="753" y="553">AROUSAL</tspan><tspan x="753" y="575">REGULATION</tspan></text>

        <text class="slice-label handler large" text-anchor="end" style="text-anchor:end"><tspan x="486" y="637">DOG</tspan><tspan x="486" y="668">SAFETY</tspan></text>
        <text class="slice-label handler" ><tspan x="539" y="725">SEARCH</tspan><tspan x="539" y="753">COVERAGE</tspan></text>
        <text class="slice-label handler" style="font-size:22px"><tspan x="662" y="715">MINIMAL</tspan><tspan x="662" y="740">NECESSARY</tspan><tspan x="662" y="765">INVOLVEMENT</tspan></text>
        <text class="slice-label handler large" style="text-anchor:start"><tspan x="703" y="637">READ</tspan><tspan x="703" y="668">THE DOG</tspan></text>
      </g>

      <!-- zone labels and inner guide arcs -->
      <text class="zone-label"><textPath href="#tp-dog-foundations" startOffset="50%" text-anchor="middle">DOG FOUNDATIONS</textPath></text>
      <text class="zone-label"><textPath href="#tp-handler-foundations" startOffset="50%" text-anchor="middle">HANDLER FOUNDATIONS</textPath></text>
      <path class="inner-arc" d="M415 766.6 A249 249 0 0 1 436.7 412.1"/>
      <path class="inner-arc" d="M766.6 414.9 A249 249 0 0 1 791.9 758.7"/>
    </g>
  </defs>

  <!-- faint enlarged backdrop of the wheel -->
  <g class="backdrop">
    <use href="#wheel-core" transform="translate(600 600) scale(2.1) translate(-600 -600)"/>
  </g>
  <circle cx="600" cy="600" r="470" fill="var(--white)"/>

  <!-- main wheel -->
  <use href="#wheel-core"/>

  <!-- operational capability area cycle -->
  <g class="cycle">
    <path class="cycle-arc" d="M163.6 576.4 A437 437 0 0 1 1036.4 576.4"/>
    <circle class="cycle-dot" cx="163.6" cy="576.4" r="5"/>
    <polyline class="cycle-head" points="1028.5,566 1036.4,577.5 1044.5,566"/>
    <path class="cycle-arc" d="M1036.3 624.4 A437 437 0 0 1 163.7 624.4"/>
    <circle class="cycle-dot" cx="1036.3" cy="624.4" r="5"/>
    <polyline class="cycle-head" points="155.8,634.5 163.7,623 171.6,634.5"/>
    <text class="area-label"><textPath href="#tp-area-top" startOffset="50%" text-anchor="middle">OPERATIONAL CAPABILITY AREA</textPath></text>
    <text class="area-label"><textPath href="#tp-area-bottom" startOffset="50%" text-anchor="middle">OPERATIONAL CAPABILITY AREA</textPath></text>
  </g>

  <!-- hub with business name -->
  <g class="hub-group">
    <circle class="hub" cx="600" cy="600" r="90"/>
    <text class="hub-name" x="600" y="600">ARVO 7</text>
  </g>
</svg>
</body>
</html>
```